Harborline Bridal Bakery Selling Method needs finishing touches to website.

We have a temporary website located at http://www.brivantomarketworks.com/ql/.
We are doing a responsive design and have created the architecture (layout). However, we need a professional makeover for the graphic elements and colors of the website. The website will be selling a sales course to mostly women who sell wedding cakes.
The photos within the posted website are for illustrative purposes. We will use our own photos after the website is redone.
We are open to changing the font styles, borders, header, and anything else as long as the layout is not changed.
Target Market(s)
75% women age 25-50 and men 30-60.
Industry/Entity Type
Architecture
Colors
Designer to choose colors to be used in the design.
Look and feel
Each slider illustrates characteristics of the customer's brand and the style your logo design should communicate.

```html
<!DOCTYPE html>
<html lang="en">
<head>
<meta charset="utf-8">
<title>Harborline Bridal Bakery Selling Method</title>
<link href="https://fonts.googleapis.com/css2?family=Roboto:wght@400;500&display=swap" rel="stylesheet">
<style>
:root{
  --orange:#e07f35;
  --orange-foot:#df873f;
  --panel-top:#f2b47f;
  --panel-bottom:#ec8630;
  --grey-bg:#ebebeb;
  --white:#ffffff;
  --text:#555555;
  --nav-text:#444444;
  --badge:#a3a3a3;
  --player:#1b2a33;
  --accent-red:#e84a5f;
}
*{box-sizing:border-box;margin:0;padding:0}
html,body{width:1200px;height:1170px;overflow:hidden}
body{font-family:'Roboto',sans-serif;background:var(--grey-bg);position:relative}
.abs{position:absolute}
.site-header{left:0;top:0;width:1200px;height:116px;background:var(--white);box-shadow:0 3px 5px rgba(0,0,0,.25);z-index:2}
.brand{left:176px;top:37px;color:var(--orange);font-size:19px;font-weight:500;line-height:26px;text-transform:uppercase}
.main-nav{left:519px;top:48px;height:29px;display:flex;align-items:center;font-size:13px;color:var(--nav-text)}
.main-nav a{color:inherit;text-decoration:none;white-space:nowrap}
.nav-home{background:linear-gradient(#f4a565,#ea8433);color:var(--white)!important;width:67px;height:29px;border-radius:3px;display:flex;align-items:center;justify-content:center}
.video{left:176px;top:163px;width:539px;height:303px;border-radius:4px;overflow:hidden;background:#000}
.video-frame{left:31px;top:0;width:477px;height:259px;background:linear-gradient(135deg,#6b5a47,#9a8468 55%,#5b4d3e)}
.play{left:212px;top:80px}
.controls{left:0;top:259px;width:539px;height:44px;background:var(--player)}
.optin{left:726px;top:160px;width:305px;height:307px;background:linear-gradient(var(--panel-top),var(--panel-bottom))}
.optin h2{position:absolute;left:22px;top:22px;width:270px;color:var(--white);font-size:13px;font-weight:400;line-height:19px;text-transform:uppercase}
.field{position:absolute;left:22px;width:261px;height:39px;background:var(--white);border:1px solid #d9d9d9;font-size:10.5px;color:#777;padding:0 10px;display:flex;align-items:center}
.cta{position:absolute;left:76px;top:218px;width:142px;height:33px;border-radius:3px;background:linear-gradient(#f6f6f6,#d6d6d6);color:#444;font-size:11px;display:flex;align-items:center;justify-content:center;box-shadow:0 1px 2px rgba(0,0,0,.2)}
.nospam{position:absolute;left:0;top:268px;width:305px;text-align:center;color:var(--white);font-size:11.5px}
.press{left:0;top:528px;width:1200px;height:120px;background:var(--white);box-shadow:0 0 6px rgba(0,0,0,.15)}
.press-badge{position:absolute;background:var(--badge);opacity:.8}
.section-title{left:0;top:678px;width:1200px;text-align:center;color:var(--orange);font-size:19px;font-weight:400;text-transform:uppercase}
.technique{width:260px;text-align:center}
.technique-photo{width:162px;height:162px;border-radius:50%;border:4px solid var(--orange);margin:0 auto}
.technique p{margin-top:26px;font-size:13.5px;line-height:19px;color:var(--text)}
.site-footer{left:0;top:1007px;width:1200px;height:163px;background:var(--orange-foot);color:var(--white)}
.footer-nav{position:absolute;left:0;top:37px;width:1200px;text-align:center;font-size:12.5px}
.footer-nav span{margin:0 9px}
.contact{position:absolute;left:176px;top:85px;font-size:12.5px}
.copyright{position:absolute;left:175px;top:112px;font-size:11.5px}
.social{position:absolute;width:36px;height:36px;border-radius:50%;background:var(--white);top:86px}
</style>
</head>
<body>

<header class="site-header abs">
  <div class="brand abs">Brivanto<br>Marketworks</div>
  <nav class="main-nav abs">
    <a class="nav-home" href="#">HOME</a>
    <a href="#" style="margin-left:15px">WHO IS QUINN LARKIN</a>
    <a href="#" style="margin-left:26px">WHY QUINN IS SHARING HER SECRETS</a>
    <a href="#" style="margin-left:26px">CONTACT</a>
  </nav>
</header>

<div class="video abs">
  <div class="video-frame abs" role="img" aria-label="Video still: equipment cases laid out on a patterned carpet"></div>
  <svg class="play abs" width="82" height="82" viewBox="0 0 82 82">
    <circle cx="41" cy="41" r="39" fill="rgba(20,20,20,.75)" stroke="rgba(255,255,255,.25)" stroke-width="2"/>
    <path d="M32 24 L60 41 L32 58 Z" fill="#fff"/>
  </svg>
  <svg class="controls abs" width="539" height="44" viewBox="0 0 539 44">
    <circle cx="27" cy="22" r="9.5" fill="none" stroke="#fff" stroke-width="2"/>
    <path d="M24 17 L32 22 L24 27 Z" fill="#fff"/>
    <path d="M57 18 h4 l5 -4 v16 l-5 -4 h-4 z" fill="var(--accent-red)"/>
    <path d="M69 17 q4 5 0 10" fill="none" stroke="var(--accent-red)" stroke-width="1.6"/>
    <g fill="var(--accent-red)">
      <rect x="81" y="17" width="2.5" height="10"/><rect x="86" y="17" width="2.5" height="10"/>
      <rect x="91" y="17" width="2.5" height="10"/><rect x="96" y="17" width="2.5" height="10"/>
      <rect x="101" y="17" width="2.5" height="10"/>
    </g>
    <g fill="#6a7780"><rect x="106" y="17" width="2.5" height="10"/><rect x="111" y="17" width="2.5" height="10"/></g>
    <rect x="136" y="20" width="235" height="4" rx="2" fill="#4a5961"/>
    <rect x="136" y="20" width="83" height="4" rx="2" fill="var(--accent-red)"/>
    <text x="388" y="27" fill="#fff" font-family="Roboto, sans-serif" font-size="12.5">01:30 / 04:55</text>
    <rect x="476" y="17" width="14" height="10" fill="none" stroke="#fff" stroke-width="2"/>
    <circle cx="513" cy="22" r="5" fill="none" stroke="#fff" stroke-width="3" stroke-dasharray="2.5 1.4"/>
    <circle cx="513" cy="22" r="2" fill="#fff"/>
  </svg>
</div>

<form class="optin abs">
  <h2>Free videos to help you sell more wedding cakes at higher prices... immediately</h2>
  <div class="field" style="top:101px">NAME</div>
  <div class="field" style="top:155px">EMAIL</div>
  <div class="cta">GET INSTANT ACCESS</div>
  <div class="nospam">NO SPAM. I PROMISE.</div>
</form>

<section class="press abs" aria-label="As featured in">
  <div class="press-badge" style="left:177px;top:42px;width:120px;height:47px"></div>
  <div class="press-badge" style="left:366px;top:44px;width:54px;height:44px"></div>
  <div class="press-badge" style="left:486px;top:55px;width:149px;height:24px;border-radius:3px"></div>
  <div class="press-badge" style="left:704px;top:42px;width:47px;height:47px"></div>
  <div class="press-badge" style="left:820px;top:42px;width:46px;height:46px;border-radius:50%"></div>
  <div class="press-badge" style="left:930px;top:50px;width:100px;height:36px"></div>
</section>

<h1 class="section-title abs">3 Leading-edge techniques for convincing brides to choose you</h1>

<div class="technique abs" style="left:157px;top:738px">
  <div class="technique-photo" role="img" aria-label="Photo of a white tiered wedding cake with red dots and a couple topper" style="background:radial-gradient(circle at 50% 60%,#f6f1ef,#e8dcd8 60%,#c9aaa6)"></div>
  <p>In the first video, discover a sales growth secret that reveals the "Two Faces Of Your Wedding Cake Business."</p>
</div>
<div class="technique abs" style="left:469px;top:738px">
  <div class="technique-photo" role="img" aria-label="Artistic portrait photo in cool blue and grey tones" style="background:radial-gradient(circle,#d9d4d2,#9aa7b4 65%,#3e5566)"></div>
  <p>In the first video, discover a sales growth secret that reveals the "Two Faces Of Your Wedding Cake Business."</p>
</div>
<div class="technique abs" style="left:772px;top:738px">
  <div class="technique-photo" role="img" aria-label="Portrait photo of a smiling woman in a red blouse" style="background:linear-gradient(#f4f2ef 45%,#d23a34 70%,#b7231f)"></div>
  <p>In the first video, discover a sales growth secret that reveals the "Two Faces Of Your Wedding Cake Business."</p>
</div>

<footer class="site-footer abs">
  <nav class="footer-nav">
    Home<span>|</span>Who Is Quinn Larkin<span>|</span>Why Quinn Is Sharing Her Secrets<span>|</span>Contact
  </nav>
  <div class="contact">Phone: 555.214.0397</div>
  <div class="copyright">Copyright © 2014 The Sugar Loft</div>
  <div class="social" style="left:856px"></div>
  <div class="social" style="left:901px"></div>
  <div class="social" style="left:945px"></div>
  <div class="social" style="left:990px"></div>
</footer>

</body>
</html>
```